Non fiction leadership Book Cover design needed for “Keep Bold: Begin Owning Daily”

I need a front cover design for a new book 6 X 9 traditional non-fiction book.

Title: "Keep BOLD - Begin Owning Daily"

The subtitle is not finalized- so use 2 lines of smaller dummy text

My brand guide is attached (please use the tan color sparingly)

I'd like to see BOLD look like it is in motion and "flying" across the page

Need CREATIVE designs and options

Do not want my picture on the front cover - I do want it on the back cover.

On the front cover I’d like to see creative use of font to create movement on “BOLD”

Target Market(s)

Business leaders

Industry/Entity Type

Aviation

Font styles to use
Other font styles liked:
• See style guide- can add additional font (modern script or san serif)

Colors
0054AA
0677BA
7BADD7
CADEEF
E8F1F8
EB3D1F
EC4F4E
F09395
F8D3D4
FCEDEE

Requirements
Must have
• Creative font use, using perspective to create movement/motion on BOLD
Should not have
• My picture on the front cover- my picture should be on the back cover

```html
<!DOCTYPE html>
<html lang="en">
<head>
<meta charset="UTF-8">
<title>Keep BOLD - Begin Owning Daily</title>
<link href="https://fonts.googleapis.com/css2?family=Rubik:wght@800;900&family=Roboto+Condensed:wght@700&family=Montserrat:wght@700&family=Nunito+Sans:wght@400&display=swap" rel="stylesheet">
<style>
  :root {
    --paper-light: #fbfaf4;
    --paper-cool: #eceef0;
    --tan-dark: #9c5e2e;
    --tan-mid: #c98d55;
    --tan-light: #ecc08c;
    --navy: #131a38;
    --red: #c0202a;
    --blue-deep: #0054aa;
    --blue-mid: #0677ba;
    --blue-soft: #7badd7;
  }
  * { margin: 0; padding: 0; box-sizing: border-box; }
  html, body { width: 800px; height: 1200px; overflow: hidden; }
  .cover {
    position: relative;
    width: 800px;
    height: 1200px;
    overflow: hidden;
    background: linear-gradient(180deg, var(--paper-light) 0%, var(--paper-light) 55%, var(--paper-cool) 100%);
  }
  .cover-art { position: absolute; left: 0; top: 0; width: 800px; height: 460px; }
  .series-word {
    position: absolute;
    left: 258px; top: 412px;
    font-family: "Rubik", sans-serif;
    font-weight: 900;
    font-size: 96px;
    line-height: 1;
    color: var(--red);
    letter-spacing: 1px;
  }
  .title-art {
    position: absolute;
    left: 0; top: 440px;
    width: 800px; height: 280px;
    overflow: visible;
  }
  .title-word {
    font-family: "Rubik", sans-serif;
    font-weight: 900;
    font-size: 200px;
  }
  .speed-line { stroke-linecap: round; }
  .title-tagline {
    position: absolute;
    left: 164px; top: 716px;
    font-family: "Roboto Condensed", sans-serif;
    font-weight: 700;
    font-size: 48px;
    line-height: 1;
    color: var(--navy);
  }
  .subtitle {
    position: absolute;
    left: 0; width: 800px; top: 828px;
    text-align: center;
    font-family: "Roboto Condensed", sans-serif;
    font-weight: 700;
    font-size: 58px;
    line-height: 1;
    color: var(--red);
  }
  .secondary-title {
    position: absolute;
    left: 0; width: 800px; top: 914px;
    text-align: center;
    font-family: "Montserrat", sans-serif;
    font-weight: 700;
    font-size: 21px;
    color: var(--navy);
  }
  .body-copy {
    position: absolute;
    left: 0; width: 800px; top: 958px;
    text-align: center;
    font-family: "Nunito Sans", sans-serif;
    font-size: 20px;
    line-height: 28px;
    color: var(--navy);
  }
  .author-band { position: absolute; left: 0; top: 1089px; width: 800px; height: 46px; }
  .author-bar-left, .author-bar-right {
    position: absolute; top: 0; height: 46px;
    background: linear-gradient(90deg, var(--tan-dark), var(--tan-light));
  }
  .author-bar-left { left: 0; width: 44px; }
  .author-bar-right { left: 608px; width: 192px; }
  .author-name {
    position: absolute;
    left: 70px; top: 0;
    line-height: 46px;
    font-family: "Montserrat", sans-serif;
    font-weight: 700;
    font-size: 36px;
    letter-spacing: 9px;
    color: var(--navy);
    white-space: nowrap;
  }
</style>
</head>
<body>
  <main class="cover">
    <svg class="cover-art" viewBox="0 0 800 460">
      <defs>
        <linearGradient id="tanSweep" x1="0" y1="0" x2="1" y2="0">
          <stop offset="0" stop-color="#9c5e2e"/>
          <stop offset="1" stop-color="#ecc08c"/>
        </linearGradient>
        <linearGradient id="flightTone" x1="0" y1="1" x2="1" y2="0">
          <stop offset="0" stop-color="#4a4f58" stop-opacity="0.35"/>
          <stop offset="0.45" stop-color="#b77d47" stop-opacity="0.55"/>
          <stop offset="1" stop-color="#e3b07a" stop-opacity="0.6"/>
        </linearGradient>
      </defs>
      <polygon class="corner-sweep" points="0,0 536,0 0,220" fill="url(#tanSweep)"/>
      <polygon class="light-streak" points="0,330 800,60 800,90 0,360" fill="#ffffff" opacity="0.8"/>
      <g role="img" aria-label="Formation of helicopter silhouettes flying diagonally upward, one large tan helicopter leading three small dark ones">
        <polygon points="40,400 720,20 790,150 300,350 60,420" fill="url(#flightTone)"/>
      </g>
    </svg>

    <div class="series-word">KEEP</div>

    <svg class="title-art" viewBox="0 0 800 280" role="img" aria-label="BOLD">
      <defs>
        <linearGradient id="boldTan" x1="0" y1="0" x2="1" y2="0">
          <stop offset="0" stop-color="#9c5e2e"/>
          <stop offset="0.24" stop-color="#ecc08c"/>
          <stop offset="0.26" stop-color="#9c5e2e"/>
          <stop offset="0.5" stop-color="#ecc08c"/>
          <stop offset="0.52" stop-color="#9c5e2e"/>
          <stop offset="0.74" stop-color="#ecc08c"/>
          <stop offset="0.76" stop-color="#9c5e2e"/>
          <stop offset="1" stop-color="#ecc08c"/>
        </linearGradient>
      </defs>
      <g class="speed-lines">
        <line class="speed-line" x1="60" y1="96" x2="150" y2="96" stroke="var(--blue-deep)" stroke-width="10"/>
        <line class="speed-line" x1="20" y1="140" x2="140" y2="140" stroke="var(--blue-mid)" stroke-width="8"/>
        <line class="speed-line" x1="70" y1="184" x2="135" y2="184" stroke="var(--blue-soft)" stroke-width="8"/>
        <line class="speed-line" x1="40" y1="228" x2="128" y2="228" stroke="var(--blue-mid)" stroke-width="6"/>
      </g>
      <g transform="translate(165 268) scale(1 1.46) skewX(-8)">
        <text class="title-word" x="0" y="0" textLength="480" lengthAdjust="spacingAndGlyphs" fill="url(#boldTan)">BOLD</text>
      </g>
    </svg>

    <div class="title-tagline">BEGIN OWNING DAILY</div>

    <h2 class="subtitle">SUBTITLE PLACEHOLDER</h2>
    <p class="secondary-title">Smaller Secondary Title Placeholder</p>
    <p class="body-copy">Nunito Sans Font Family for All Body Copy -<br>Lorem ipsum dolor sit amet, consectetur adipiscing elit.</p>

    <div class="author-band">
      <span class="author-bar-left"></span>
      <span class="author-name">Margaret Ellison</span>
      <span class="author-bar-right"></span>
    </div>
  </main>
</body>
</html>
```